Creative Labels needed for Pellway Cleaning Products

Four bottle labels 5.25 inches tall by 7 inches wide, Two packaging labels 4.375 inches tall by 4.5 inches wide. Basic Information on each labels including basic color scheme is attached - ok to change color scheme. Would like to add the words "Pellway Cleaning" somewhere on the two packaging labels and have the overall design hint at craft beer, perhaps something along the lines of Varo Beer Labels (picture of this is attached) with a feminine touch and perhaps just a hint of the east (India/yoga/essential oils) and nature (plants/flowers). All labels will also need barcodes which are attached. Please make sure correct barcode is on correct label. The "packaging label barcode" is used twice - the same barcode on the two different "packaging" labels. All art is on clear background, so to my understanding all art and fonts need a white layer underneath.

Target Market(s)

age - 20s - 60s
location - urban
gender - all
income level - 40K and up
marital or family status - any
occupation - any
ethnic background - any
interests - natural health and wellness, yoga, essential oils, health food, craft beer, music, art, travel

Industry/Entity Type

Cleaning Product

Font styles to use
Decorative

Colors

Designer to choose colors to be used in the design.

Requirements
Must have
• See description. Please note there are 6 different labels. They will all have the same look, and there are only 2 different sizes involved. There are distinctions between each label as noted in the pictures submitted. Open to some budget adjustments if discussed/needed because of these 6 variations.
Nice to have
• See description, plus some clear space on the labels, as they will be printed on clear labels and placed on clear bottles.

```html
<!DOCTYPE html>
<html lang="en">
<head>
<meta charset="utf-8">
<title>Hamo Glass Cleaner Label</title>
<link rel="stylesheet" href="https://fonts.googleapis.com/css2?family=Black+Ops+One&family=Cinzel:wght@700;900&family=Oswald:wght@600;700&display=swap">
<style>
  :root {
    --amber: #d49a1a;
    --amber-deep: #b9800f;
    --amber-light: #e2ac2c;
    --label-white: #fbf8ef;
    --cleaner-red: #c0142e;
  }
  html, body {
    margin: 0;
    padding: 0;
    width: 1200px;
    height: 2400px;
    overflow: hidden;
  }
  body {
    background: linear-gradient(90deg, var(--amber-deep) 0%, var(--amber) 20%, var(--amber-light) 55%, var(--amber) 100%);
  }
  .label-art {
    display: block;
    width: 1200px;
    height: 2400px;
  }
  .brand-name {
    font-family: "Cinzel", serif;
    font-weight: 900;
    font-size: 96px;
    fill: var(--label-white);
  }
  .tagline {
    font-family: "Oswald", sans-serif;
    font-weight: 700;
    font-size: 50px;
    fill: var(--label-white);
  }
  .product-name {
    font-family: "Black Ops One", sans-serif;
    font-size: 142px;
    fill: var(--cleaner-red);
    stroke: var(--label-white);
    stroke-width: 8px;
    paint-order: stroke;
  }
  .strength {
    font-family: "Cinzel", serif;
    font-weight: 700;
    font-size: 62px;
    fill: var(--label-white);
  }
  .volume {
    font-family: "Oswald", sans-serif;
    font-weight: 700;
    font-size: 46px;
    fill: var(--label-white);
  }
  .power-note {
    font-family: "Oswald", sans-serif;
    font-weight: 700;
    font-size: 38px;
    fill: var(--amber);
  }
  .yield-line {
    font-family: "Oswald", sans-serif;
    font-weight: 700;
    font-size: 46px;
    fill: var(--amber);
    letter-spacing: 2px;
  }
</style>
</head>
<body>
<svg class="label-art" viewBox="0 0 1200 2400" xmlns="http://www.w3.org/2000/svg">
  <defs>
    <clipPath id="badge-inner">
      <circle cx="600" cy="1392" r="308"/>
    </clipPath>
    <path id="yield-arc" d="M 262 1392 A 338 338 0 0 0 938 1392"/>
  </defs>

  <!-- sunflower emblem area -->
  <circle class="flower-emblem" cx="620" cy="1008" r="384" fill="#ffffff" fill-opacity="0.22" role="img" aria-label="Outlined sunflower illustration behind the brand name"/>

  <text class="brand-name" x="600" y="995" text-anchor="middle">Hamo</text>
  <text class="tagline" x="600" y="1078" text-anchor="middle">Make Your Own</text>

  <!-- product name banner -->
  <path class="name-banner" d="M 110 1101 L 1090 1101 A 30 30 0 0 0 1120 1131 L 1120 1266 A 30 30 0 0 0 1090 1296 L 110 1296 A 30 30 0 0 0 80 1266 L 80 1131 A 30 30 0 0 0 110 1101 Z" fill="var(--amber)" stroke="var(--label-white)" stroke-width="12"/>
  <text class="product-name" x="600" y="1252" text-anchor="middle" textLength="880" lengthAdjust="spacingAndGlyphs">Glass Cleaner</text>

  <text class="strength" x="600" y="1370" text-anchor="middle" textLength="740" lengthAdjust="spacingAndGlyphs">Super Concentrated</text>

  <!-- lower badge -->
  <path class="badge-ring" d="M 232 1392 A 368 368 0 0 0 968 1392 L 908 1392 A 308 308 0 0 1 292 1392 Z" fill="var(--label-white)"/>
  <line x1="232" y1="1392" x2="968" y2="1392" stroke="var(--label-white)" stroke-width="14"/>
  <g clip-path="url(#badge-inner)">
    <path class="badge-rays" d="M 292 1392 L 600 1540 L 908 1392 L 908 1720 L 292 1720 Z" fill="#ffffff" fill-opacity="0.55" role="img" aria-label="Sunburst ray pattern inside the badge"/>
  </g>
  <polyline points="292,1392 600,1540 908,1392" fill="none" stroke="var(--label-white)" stroke-width="12"/>

  <text class="volume" x="600" y="1462" text-anchor="middle">16oz</text>

  <g class="power-stamp" transform="rotate(-6 840 1495)">
    <rect x="752" y="1418" width="176" height="154" rx="18" fill="var(--label-white)"/>
    <text class="power-note" x="840" y="1464" text-anchor="middle">16X</text>
    <text class="power-note" x="840" y="1510" text-anchor="middle">Cleaning</text>
    <text class="power-note" x="840" y="1556" text-anchor="middle">Power</text>
  </g>

  <text class="yield-line" dy="16">
    <textPath href="#yield-arc" startOffset="50%" text-anchor="middle">Make 16 bottles</textPath>
  </text>
</svg>
</body>
</html>
```